Sports Supplements review site PSD Photoshop

Hello,

We are looking to produce a site to allow users of sports supplements to add their opinions and make reviews on the supplements they have used.
We require a site that looks very current (see: http://www.pricemythings.example/ it will essentially be a supplement review site so it must contain some nice physique images and product shots too.
I like the colours used in the Price My Things site. It will need to capture the elements of this site below but needs to look much slicker.
http://www.fuelverdicts.example
We will be adding a social media part to the site too.

Best Regards

Dean Hollister
www.titanfuelshop.example

Target Market(s)

16 to 40 year old males. Heavy gym user.

Industry/Entity Type

Media

Requirements
Must have
• Great design!

```html
<!DOCTYPE html>
<html lang="en">
<head>
<meta charset="utf-8">
<title>Titan Fuel Shop – Review</title>
<link href="https://fonts.googleapis.com/css2?family=Comfortaa:wght@400;700&family=Noto+Sans&display=swap" rel="stylesheet">
<style>
:root{
  --backdrop:#c4c4c4;
  --page:#ffffff;
  --accent:#2a9ff0;
  --accent-dark:#1577d6;
  --footer:#0a82e6;
  --navy:#0d2f6b;
  --ink:#111111;
  --rule:#cfcfcf;
  --placeholder:#c8c8c8;
  --brand:#f06a22;
}
*{box-sizing:border-box;margin:0;padding:0}
html,body{width:1200px;height:900px;overflow:hidden}
body{background:var(--backdrop);font-family:"Comfortaa",sans-serif;position:relative}
.page{position:absolute;left:76px;top:0;width:1050px;height:760px;background:var(--page);box-shadow:0 0 14px rgba(0,0,0,.35)}
.brand{position:absolute;left:142px;top:28px;display:flex;align-items:center;gap:10px;font:700 26px "Comfortaa",sans-serif;color:var(--brand)}
.brand-mark{width:30px;height:30px;background:var(--brand)}
.login{position:absolute;left:660px;top:14px}
.login-row{display:flex;align-items:center;justify-content:flex-end;height:33px}
.login-label{color:var(--accent);font-size:25px;margin-right:14px}
.login-field{width:225px;height:24px;border:1px solid #bbb;border-radius:6px;box-shadow:inset 0 2px 3px rgba(0,0,0,.15)}
.login-button{position:absolute;left:266px;top:67px;width:122px;height:27px;background:linear-gradient(#4cb3f5,var(--accent-dark));color:#fff;font-size:22px;text-align:center;line-height:27px;border-radius:2px;box-shadow:0 1px 3px rgba(0,0,0,.4)}
.nav{position:absolute;left:76px;top:120px;width:1050px;height:31px;border-top:2px solid #ddd;border-bottom:2px solid #ddd;display:flex;justify-content:center;align-items:center}
.nav a{color:var(--accent);text-decoration:none;font-size:16px;padding:0 6px;border-left:1px solid #ccc}
.nav a:first-child{border-left:none}
.card{position:absolute;left:138px;top:167px;width:958px;height:588px;background:#fff;box-shadow:0 0 5px rgba(0,0,0,.35);border-radius:2px}
.product-shot{position:absolute;left:40px;top:24px;width:119px;height:60px;background:linear-gradient(#f2f2f2,#9ba7b5);box-shadow:0 0 3px rgba(0,0,0,.4)}
.specs{position:absolute;left:8px;top:92px;font:11.5px/14.2px "Noto Sans",sans-serif;color:var(--ink)}
.review-text{position:absolute;left:187px;top:21px;width:755px;font:14.5px/14.2px "Noto Sans",sans-serif;letter-spacing:.6px;color:var(--ink)}
.divider{position:absolute;left:0;top:214px;width:958px;border-top:1px solid var(--rule)}
.avatar{position:absolute;left:15px;width:116px;height:61px;background:var(--placeholder)}
.comment{position:absolute;left:147px;width:774px;height:91px;padding:4px 12px;font-size:12.3px;line-height:16.5px;color:var(--ink);box-shadow:0 1px 5px rgba(0,0,0,.45);background:#fff}
.reply{position:absolute;width:130px;height:24px;text-align:center;font-size:18px;line-height:24px;color:var(--ink);box-shadow:0 1px 4px rgba(0,0,0,.45);background:#fff}
.footer{position:absolute;left:0;top:760px;width:1200px;height:140px;background:var(--footer)}
.footer-links{position:absolute;left:80px;top:22px;width:1000px;text-align:center;font-size:14.5px;line-height:14.2px;color:#fff;letter-spacing:.5px;text-shadow:0 0 2px #063d7a}
.copyright{position:absolute;left:280px;top:104px;font-size:25px;letter-spacing:2px;color:var(--navy)}
</style>
</head>
<body>
<div class="page"></div>

<div class="brand"><span class="brand-mark"></span>Titanfuelshop.example</div>

<div class="login">
  <div class="login-row"><span class="login-label">Username:</span><span class="login-field"></span></div>
  <div class="login-row"><span class="login-label">Password:</span><span class="login-field"></span></div>
  <div class="login-button">Login</div>
</div>

<nav class="nav">
  <a href="#">Home</a><a href="#">Forum</a><a href="#">Submit a review</a><a href="#">Categories</a><a href="#">Retailers</a><a href="#">Top Rated</a><a href="#">About</a><a href="#">Register</a>
</nav>

<main class="card">
  <div class="product-shot" role="img" aria-label="Product shot of an Amino Base BCAA tub"></div>
  <div class="specs">Pros:<br>Good For Stacking<br>Less Soreness<br>Good Value<br>Builds Muscle<br><br>Cons:<br>None</div>
  <p class="review-text">Apex Formula Labs really did a good job here. Great BCAA ratio, Great absorption, great taste. It can be used by itself or with a stack. If I find that a protein or a No boost doesn't have quite the amount of BCAA's I want i'll add a half scoop to a scoop of this stuff. The first thing your gonna notice is its texture. Its the finest powdered BCAA supplement I've ever tried. It is because of how micronized the BCAA's are along with the fact that there are so few additives that gives it this texture. Using this product I've notice an increase in energy, quicker recoveries, and more stamina in the gym. The price is great for what your getting. I got it for 20$ but most people are gonna find it for around 30-40$ but it IS worth it.</p>
  <div class="divider"></div>

  <div class="avatar" style="top:267px" role="img" aria-label="User avatar placeholder"></div>
  <p class="comment" style="top:251px">At vero eos et accusamus et iusto odio dignissimos ducimus qui blanditiis praesentium voluptatum deleniti atque corrupti quos dolores et quas molestias excepturi sint occaecati cupiditate non provident, similique sunt in culpa qui officia deserunt mollitia animi, id est laborum et dolorum fuga. Et harum quidem rerum facilis est et expedita distinctio.</p>
  <div class="reply" style="left:765px;top:350px">Reply</div>

  <div class="avatar" style="top:409px" role="img" aria-label="User avatar placeholder"></div>
  <p class="comment" style="top:393px">At vero eos et accusamus et iusto odio dignissimos ducimus qui blanditiis praesentium voluptatum deleniti atque corrupti quos dolores et quas molestias excepturi sint occaecati cupiditate non provident, similique sunt in culpa qui officia deserunt mollitia animi, id est laborum et dolorum fuga. Et harum quidem rerum facilis est et expedita distinctio.</p>
  <div class="reply" style="left:767px;top:494px">Reply</div>
</main>

<footer class="footer">
  <p class="footer-links">[Contact + Help] [Secure Ordering] [Shipping] [About Us] [Feedback] [Trade Customers Only] [Buyer's Guide] [Careers] [Frequently Asked Questions] [Returns] [Mr Iron Classic 2006] [Product of the Year 2007] [Can't Find A Product] [Product of the Year 08] [Store Locations] [Product of the Year 09] [Ask the Experts] [Halvorsen Competition] [Product of the Year 2010] [Privicy Policy] [Terms and Conditions] [Site Map]</p>
  <p class="copyright">© 2009 Titan Fuel Shop</p>
</footer>
</body>
</html>
```